Detail Shop Business card design

i need a business card design for my new detailing company called 'Brenner's Detail Shop'. i want an all black and white design . simple, direct and to the point. i want the designer to choose a fitting font to match the logothe front should have logo, address, phone and email and the back side should have a slogan and text indicating that we offer services on anything including cars, trucks, motorcycles and RVs. slogan will read "we take pride in your ride"
maybe also very small on the back side the IG icon with Brenners_Detail_Shop

phone 482.615.7734
address 7384 E Harlow Ave
Spokane WA 99342
email: BrennersDetail@quorvail.com

Target Market(s)

all ages , auto enthusiasts

Industry/Entity Type

Automotive

Contact Information for Business Card

the front should have logo, address, phone and email and the back side should have a slogan and text indicating that we offer services on anything including cars, trucks, motorcycles and RVs. slogan will read "we take pride in your ride"

phone 482.615.7734
address 7384 E Harlow Ave
Spokane WA 99342

Colors
000000
ffffff

Requirements
Must have
• bold font and very simple design with good spacing
Nice to have
• anything creative from the designer indicating we service any types of vehicles
Should not have
• any colors ,

```html
<!DOCTYPE html>
<html lang="en">
<head>
<meta charset="utf-8">
<title>Brenner's Detail Shop – Business Card</title>
<link href="https://fonts.googleapis.com/css2?family=Arimo:wght@400;700&family=Courgette&family=Rokkitt:wght@800&display=swap" rel="stylesheet">
<style>
  :root {
    --stage: #1c1c1c;
    --card: #0e0e0e;
    --card-edge: #151515;
    --ink: #ffffff;
    --rule: #cfcfcf;
    --ghost: rgba(255,255,255,0.05);
  }
  * { margin: 0; padding: 0; box-sizing: border-box; }
  html, body { width: 1200px; height: 1200px; overflow: hidden; }
  body {
    background: radial-gradient(circle at 50% 40%, #2a2a2a 0%, var(--stage) 70%);
    display: flex; flex-direction: column; align-items: center; justify-content: center;
    gap: 40px;
    font-family: "Arimo", Arial, sans-serif;
    color: var(--ink);
  }
  .card {
    position: relative;
    width: 960px; height: 540px;
    border-radius: 22px;
    background: linear-gradient(135deg, var(--card-edge), var(--card));
    box-shadow: 0 20px 40px rgba(0,0,0,0.55);
    overflow: hidden;
  }
  .rule { height: 1px; background: var(--rule); }

  /* Back */
  .back-stack {
    position: absolute; left: 70px; right: 70px; top: 120px;
    display: flex; flex-direction: column; align-items: stretch;
  }
  .slogan-row, .handle-row {
    display: flex; align-items: center; gap: 20px;
  }
  .slogan-row .rule, .handle-row .rule { flex: 1; }
  .slogan {
    font-family: "Courgette", cursive;
    font-size: 38px;
    white-space: nowrap;
  }
  .services {
    margin: 28px 0 40px;
    text-align: center;
    font-family: "Rokkitt", serif;
    font-weight: 800;
    font-size: 46px;
    letter-spacing: 1px;
    white-space: nowrap;
  }
  .handle-row { margin-top: 0; }
  .handle {
    display: flex; align-items: center; gap: 12px;
    font-size: 24px; white-space: nowrap;
  }
  .handle-mark { width: 24px; height: 24px; background: var(--ink); border-radius: 5px; }
  .back-stack > .rule.bottom { margin-top: 0; }

  /* Front */
  .watermark {
    position: absolute; left: 520px; top: 110px; width: 400px;
    font-weight: 700; font-size: 60px; line-height: 1.05;
    color: var(--ghost); text-align: center; text-transform: uppercase;
  }
  .brand {
    position: absolute; left: 70px; top: 60px;
    display: flex; align-items: center; gap: 20px;
  }
  .brand-dot { width: 70px; height: 70px; border: 4px solid var(--ink); border-radius: 50%; }
  .brand-name { font-weight: 700; font-size: 36px; line-height: 1.1; text-transform: uppercase; }
  .person { position: absolute; left: 70px; top: 220px; }
  .person-name { font-size: 36px; letter-spacing: 2px; text-transform: uppercase; }
  .person-role { font-size: 22px; letter-spacing: 1px; text-transform: uppercase; margin-top: 2px; }
  .front-rule { position: absolute; left: 70px; width: 820px; top: 310px; }
  .contact { position: absolute; left: 70px; top: 330px; font-size: 26px; }
  .contact-row { display: flex; align-items: center; gap: 14px; margin-bottom: 10px; }
  .contact-row svg { width: 22px; height: 22px; fill: var(--ink); }
  .address {
    position: absolute; right: 70px; bottom: 50px;
    text-align: right; font-size: 26px; line-height: 1.35; font-style: normal;
  }
</style>
</head>
<body>

<section class="card card-back">
  <div class="back-stack">
    <div class="slogan-row">
      <span class="rule"></span>
      <p class="slogan">Taking pride in your ride</p>
      <span class="rule"></span>
    </div>
    <p class="services">AUTO • MOTORCYCLE • BOATS • RVS</p>
    <div class="handle-row">
      <span class="rule"></span>
      <div class="handle"><span class="handle-mark"></span><span>Brenners_Detail_Shop</span></div>
      <span class="rule"></span>
    </div>
  </div>
</section>

<section class="card card-front">
  <div class="watermark" aria-hidden="true">Brenner's<br>Detail Shop</div>
  <div class="brand">
    <span class="brand-dot"></span>
    <span class="brand-name">Brenner's<br>Detail Shop</span>
  </div>
  <div class="person">
    <p class="person-name">Dylan Marsh</p>
    <p class="person-role">Owner</p>
  </div>
  <div class="rule front-rule"></div>
  <div class="contact">
    <div class="contact-row">
      <svg viewBox="0 0 24 24" aria-hidden="true"><path d="M6.6 10.8a15.1 15.1 0 0 0 6.6 6.6l2.2-2.2a1 1 0 0 1 1-.25 11.4 11.4 0 0 0 3.6.57 1 1 0 0 1 1 1V20a1 1 0 0 1-1 1A17 17 0 0 1 3 4a1 1 0 0 1 1-1h3.5a1 1 0 0 1 1 1c0 1.25.2 2.45.57 3.57a1 1 0 0 1-.25 1z"/></svg>
      <span>482.615.7734</span>
    </div>
    <div class="contact-row">
      <svg viewBox="0 0 24 24" aria-hidden="true"><path d="M2 5h20v14H2z M3.5 6.5v.4L12 13l8.5-6.1v-.4z" fill-rule="evenodd"/></svg>
      <span>BrennersDetail@quorvail.com</span>
    </div>
  </div>
  <address class="address">7384 E Harlow Ave<br>Spokane WA 99342</address>
</section>

</body>
</html>
```